Korvel Staffing Full Length Retractable Office Banner

I need a design for a full-length retractable banner and A-Frame Sign for each of my offices. I have included designs that have been incorporated into a poster and tri-fold as a sample. I would like to see a colorful eyecatching banner that focuses on people. Would like to see some diversity with men and woman and different races.
Korvel Staffing is a light industrial staffing firm. www.KorvelStaffing.example

Target Market(s)

Job seekers looking for employment

Industry/Entity Type

Staffing / Recruiting

Font styles to use
Other font styles liked:
• Professional yet fun

Requirements
Must have
• Eye catching design with young hip vibe.
Nice to have
• primary colors with light industrial type jobs

```html
<!DOCTYPE html>
<html lang="en">
<head>
<meta charset="utf-8">
<title>Korvel Staffing – Retractable Banner</title>
<link href="https://fonts.googleapis.com/css2?family=Oswald:wght@400;500;600&family=Roboto:wght@400;700&display=swap" rel="stylesheet">
<style>
  :root {
    --backdrop: #666666;
    --banner: #f7f7f2;
    --navy: #2b2a63;
    --red: #e12b2e;
    --green: #1f7a3a;
    --yellow: #f0cf12;
    --orange: #f58f22;
    --rule: #555555;
    --crowd-a: #d8cfc4;
    --crowd-b: #8fb8c4;
  }
  * { box-sizing: border-box; margin: 0; padding: 0; }
  html, body { width: 1200px; height: 930px; overflow: hidden; }
  body { background: var(--backdrop); position: relative; }

  .banner {
    position: absolute;
    left: 411px; top: 20px;
    width: 378px; height: 890px;
    background: var(--banner);
    text-align: center;
  }
  .banner > * { position: absolute; left: 0; right: 0; }

  .brand-name {
    top: 82px;
    font-family: "Oswald", sans-serif;
    font-weight: 600;
    font-size: 44px;
    color: var(--navy);
    letter-spacing: 1px;
  }

  .headline-connecting {
    top: 212px;
    font-family: "Oswald", sans-serif;
    font-weight: 600;
    font-size: 60px;
    line-height: 1;
    color: var(--navy);
  }
  .headline-people {
    top: 284px;
    font-family: "Roboto", sans-serif;
    font-size: 40px;
    line-height: 1;
    color: var(--red);
  }
  .headline-people strong { font-weight: 700; }
  .headline-with {
    top: 330px;
    font-family: "Roboto", sans-serif;
    font-size: 24px;
    line-height: 1;
    color: var(--navy);
  }
  .headline-orgs {
    top: 355px;
    font-family: "Oswald", sans-serif;
    font-weight: 500;
    font-size: 35px;
    line-height: 1.1;
    color: var(--green);
  }

  .divider { top: 409px; left: 44px; right: 44px; height: 1px; background: var(--rule); }
  .divider-accent { top: 407px; left: 169px; right: 169px; height: 4px; background: var(--red); }

  .hiring {
    top: 416px;
    font-family: "Oswald", sans-serif;
    font-weight: 600;
    font-size: 50px;
    line-height: 1.1;
    color: var(--orange);
  }

  .colour-bands { top: 486px; height: 6px; display: flex; gap: 2px; }
  .colour-bands span { flex: 1; }
  .band-red { background: var(--red); }
  .band-green { background: var(--green); }
  .band-yellow { background: var(--yellow); }
  .band-navy { background: var(--navy); }

  .web-address {
    top: 514px;
    font-family: "Roboto", sans-serif;
    font-size: 15px;
    letter-spacing: 3.5px;
    color: var(--navy);
  }
  .web-address .domain { color: var(--red); }

  .crowd-photo {
    top: 595px; left: 21px; right: 13px; height: 215px;
    border-radius: 40% 40% 30% 30% / 20% 20% 50% 50%;
    background: radial-gradient(ellipse at 50% 60%, var(--crowd-b) 0%, var(--crowd-a) 55%, var(--banner) 80%);
  }
</style>
</head>
<body>
  <main class="banner">
    <div class="brand-name">Korvel Staffing</div>
    <h1 class="headline-connecting">CONNECTING</h1>
    <p class="headline-people"><strong>GREAT</strong> PEOPLE</p>
    <p class="headline-with">WITH</p>
    <p class="headline-orgs">GREAT ORGANIZATIONS!</p>
    <div class="divider"></div>
    <div class="divider-accent"></div>
    <p class="hiring">ALWAYS HIRING</p>
    <div class="colour-bands">
      <span class="band-red"></span><span class="band-green"></span><span class="band-yellow"></span><span class="band-navy"></span>
    </div>
    <p class="web-address">www.<span class="domain">KorvelStaffing</span>.example</p>
    <div class="crowd-photo" role="img" aria-label="Photograph of a large, diverse crowd of men and women standing together and looking up"></div>
  </main>
</body>
</html>
```